Personal Training Studio Checkin App (or URL based)

I would like a simple web based app built for our  business. We have a training studio with a simple business model. All our clients buy sessions in packages either 4, 8, or 12 at a time. We want something that a trainer can pull up and Check in a client. This will record the date and time the client was checked in, by what trainer, and what type of session. This system will keep track of the following:
Whenever a Client Checks in so it will ‘tick off’ a session on their package (ie- they have gone from 11 sessions left to 10 sessions left)
Track what sessions a particular trainer does so we can pay them at the end of the week and look at who they trained, what type of session and how many
Look at client activity: Every time they check in, Recharge their package, any activity related to the client, even if it was admin – like deleting a session that was mistakenly recorded.
This will keep a database of clients added and all their activity
The pdf I have included lays out how I think it would work and the features I want
I would like this to run off an tablora that we have at our front check in counter. It can be an app or a URL that use.
***THIS PROJECT IS NOT SO MUCH ABOUT DESIGN BUT ABOUT FUNCTIONALITY OF THE APPLICATION. IT MUST HAVE THE FEATURES I HAVE ASKED FOR THAT WORK TOGETHER. I AM WILLING TO PAY A LITTLE MORE AS A BONUS IF YOU CAN ACCOMPLISH THIS. ALSO IF I FIN THE RIGHT PERSON THAT CAN DO THIS I WILL MAKE IT A GUARNTEED PROJECT.

- Functionality and Track and record all the info we need

```html
<!DOCTYPE html>
<html lang="en">
<head>
<meta charset="utf-8">
<title>Corestride Personal Training Studio – Session Types</title>
<link rel="stylesheet" href="https://fonts.googleapis.com/css2?family=Poppins:wght@300;400;500;600&display=swap">
<style>
:root{
  --orange:#ff4a00;
  --navy:#262a63;
  --card:#e6e8fb;
  --card-text:#555763;
  --card-num:#c9cbe0;
  --dark:#1d1d1f;
  --grey-bar:#5a5a5c;
  --footer:#59595b;
  --ink:#1b1b1b;
  --muted:#5c5c5c;
  --rule:#e2e2e2;
  --white:#ffffff;
}
*{margin:0;padding:0;box-sizing:border-box}
html,body{width:1200px;height:1178px;overflow:hidden}
body{position:relative;font-family:"Poppins",sans-serif;background:var(--white);color:var(--ink)}
.abs{position:absolute}

/* hero */
.hero{left:0;top:0;width:1200px;height:188px;background:linear-gradient(90deg,#1b2142 0%,#23295a 45%,#3a1e3a 70%,#3b0e14 100%)}
.brand{left:131px;top:16px;width:216px;height:62px;background:var(--white);clip-path:polygon(10px 0,100% 0,calc(100% - 14px) 100%,0 100%);border-bottom:3px solid var(--orange);display:flex;align-items:center;justify-content:center;gap:7px}
.brand-mark{width:12px;height:12px;background:var(--orange)}
.brand-name{font-weight:600;font-size:19px;color:#5a5a5c;letter-spacing:.5px}
.nav-primary{left:331px;top:27px;width:419px;height:40px;background:var(--orange);clip-path:polygon(14px 0,100% 0,calc(100% - 10px) 100%,0 100%)}
.nav-secondary{left:740px;top:27px;width:460px;height:40px;background:var(--grey-bar);clip-path:polygon(10px 0,100% 0,100% 100%,0 100%)}
.nav-item{top:38px;display:flex;align-items:center;gap:6px;color:var(--white);font-size:10px;font-weight:500}
.nav-icon{width:21px;height:21px;border-radius:50%;background:var(--white);display:flex;align-items:center;justify-content:center}
.nav-link{top:40px;color:var(--white);font-size:10px;font-weight:500}
.call-icon{left:934px;top:35px;width:25px;height:25px;border-radius:50%;background:var(--orange);display:flex;align-items:center;justify-content:center}
.call-text{left:964px;top:34px;color:var(--white);line-height:1.1}
.call-text small{display:block;font-size:8px}
.call-text b{font-size:11px;font-weight:600}

/* session types */
.sessions{left:0;top:188px;width:1200px;height:212px;background:var(--navy)}
.sessions-title{left:0;top:244px;width:1200px;text-align:center;color:var(--white);font-size:25px;font-weight:600}
.card{top:300px;width:212px;height:100px;background:var(--card);overflow:hidden}
.card-label{position:absolute;left:18px;top:30px;font-size:17px;font-weight:500;line-height:1.1;color:var(--card-text)}
.card-num{position:absolute;right:18px;top:8px;font-size:66px;font-weight:300;color:var(--card-num);line-height:1.2}
.card.is-active{background:var(--orange)}
.card.is-active .card-label{color:var(--white);top:24px}
.card.is-active .card-label small{display:block;font-size:10px;font-weight:400;margin-top:3px}
.card.is-active .card-num{color:#ff3a00;text-shadow:0 0 0 #e83800;opacity:.7;color:#d93600}

/* detail */
.detail{left:0;top:400px;width:1200px;height:301px;background:var(--dark)}
.detail-photo{left:612px;top:400px;width:588px;height:301px;background:linear-gradient(90deg,#1d1d1f 0%,#2f3439 25%,#4a5866 60%,#6f8496 100%)}
.pointer{left:700px;top:400px}
.detail-title{left:156px;top:444px;color:var(--orange);font-size:20px;font-weight:600}
.detail-sub{left:156px;top:470px;color:var(--white);font-size:12.5px}
.detail-copy{left:156px;top:496px;width:390px;color:#d8d8d8;font-size:10.6px;line-height:16.5px;font-weight:300}
.select-label{left:156px;top:565px;color:#a8a8a8;font-size:10px;font-weight:500}
.select{left:156px;top:587px;width:206px;height:28px;border:1px solid #5c5c5c;background:var(--dark);color:#d0d0d0;font-size:9.5px;display:flex;align-items:center;justify-content:space-between;padding:0 12px 0 10px}
.btn{left:156px;top:624px;width:121px;height:31px;background:var(--white);color:#333;font-size:12px;font-weight:500;display:flex;align-items:center;justify-content:center}

/* faq */
.faq-title{left:0;top:767px;width:1200px;text-align:center;font-size:25px;font-weight:500;color:#555}
.faq-rule{left:262px;width:675px;height:1px;background:var(--rule)}
.faq-q{left:264px;font-size:12.5px;font-weight:500;color:var(--ink)}
.faq-q.is-open{color:var(--orange)}
.faq-a{left:264px;top:910px;width:615px;font-size:11.5px;line-height:15.5px;color:#222}
.faq-toggle{left:913px;width:16px;height:16px;border-radius:50%;background:#5a5a5c;display:flex;align-items:center;justify-content:center}
.faq-toggle.is-open{background:var(--orange)}

/* footer */
.footer{left:0;top:1141px;width:1200px;height:37px;background:var(--footer)}
.copyright{left:157px;top:1152px;color:var(--white);font-size:10.6px}
.social{top:1152px;width:11px;height:11px;background:var(--white);border-radius:2px}
.social-round{left:1018px;top:1147px;width:26px;height:26px;border-radius:50%;background:var(--orange);display:flex;align-items:center;justify-content:center}
</style>
</head>
<body>

<header>
  <div class="abs hero" role="img" aria-label="Gym photo with dumbbell rack and athlete in training wear"></div>
  <div class="abs brand"><span class="brand-mark"></span><span class="brand-name">CORESTRIDE</span></div>
  <div class="abs nav-primary"></div>
  <div class="abs nav-secondary"></div>

  <div class="abs nav-item" style="left:356px">
    <span class="nav-icon"><svg width="11" height="11" viewBox="0 0 12 12"><circle cx="6" cy="4" r="2.4" fill="#ff4a00"/><path d="M1.5 11c0-2.6 2-4 4.5-4s4.5 1.4 4.5 4z" fill="#ff4a00"/></svg></span>Client Check In
  </div>
  <div class="abs nav-item" style="left:489px">
    <span class="nav-icon"><svg width="11" height="11" viewBox="0 0 12 12"><circle cx="5" cy="4" r="2.4" fill="#ff4a00"/><path d="M0.8 11c0-2.6 1.8-4 4.2-4s3 .8 3.4 1.6V11z" fill="#ff4a00"/><path d="M10 7v4M8 9h4" stroke="#ff4a00" stroke-width="1.2"/></svg></span>Add New Client
  </div>
  <div class="abs nav-item" style="left:627px">
    <span class="nav-icon"><svg width="11" height="11" viewBox="0 0 12 12"><rect x="1" y="1.5" width="10" height="9" rx="1" fill="none" stroke="#ff4a00" stroke-width="1.2"/><path d="M1 4h10M3.5 6.5h2v2h-2zM6.5 6.5h2v2h-2z" stroke="#ff4a00" stroke-width="1"/></svg></span>Admin Panel
  </div>

  <nav>
    <span class="abs nav-link" style="left:777px">Home</span>
    <span class="abs nav-link" style="left:830px">About</span>
    <span class="abs nav-link" style="left:884px">FAQs</span>
  </nav>
  <div class="abs call-icon"><svg width="12" height="12" viewBox="0 0 24 24"><path d="M6.6 10.8a15 15 0 0 0 6.6 6.6l2.2-2.2a1 1 0 0 1 1-.25 11.4 11.4 0 0 0 3.6.6 1 1 0 0 1 1 1V20a1 1 0 0 1-1 1A17 17 0 0 1 3 4a1 1 0 0 1 1-1h3.5a1 1 0 0 1 1 1c0 1.25.2 2.45.6 3.6a1 1 0 0 1-.25 1z" fill="#fff"/></svg></div>
  <div class="abs call-text"><small>Call Now</small><b>555.214.7730</b></div>
</header>

<section>
  <div class="abs sessions"></div>
  <h1 class="abs sessions-title">We have 4&nbsp; Session Types</h1>

  <div class="abs card" style="left:156px"><span class="card-label">Single<br>Session</span><span class="card-num">1</span></div>
  <div class="abs card" style="left:381px"><span class="card-label">Partner<br>Session</span><span class="card-num">2</span></div>
  <div class="abs card is-active" style="left:606px"><span class="card-label">Partner<br>Session<small>(Only 1 Party&nbsp; Showed)</small></span><span class="card-num">3</span></div>
  <div class="abs card" style="left:831px"><span class="card-label">Drop In<br>Partner</span><span class="card-num">4</span></div>
</section>

<section>
  <div class="abs detail"></div>
  <div class="abs detail-photo" role="img" aria-label="Photo of a smiling woman in sportswear leaning in a gym"></div>
  <svg class="abs pointer" width="22" height="16" viewBox="0 0 22 16"><path d="M0 0h22L11 16z" fill="#ff4a00"/></svg>

  <h2 class="abs detail-title">Partner Session</h2>
  <p class="abs detail-sub">(Only 1 Party&nbsp; Showed)</p>
  <p class="abs detail-copy">Partner Session (Only 1 Partner Showed) This Is When A People&nbsp; Who Have Bought A Partner Packaged, But Only 1 Person&nbsp; Showed Up That Day- It Is A Way For Us To Note The Trainer Only Trained One Person Not 2</p>
  <span class="abs select-label">Select Sessions To Buy:</span>
  <div class="abs select">4 Nos <svg width="7" height="4" viewBox="0 0 7 4"><path d="M0 0h7L3.5 4z" fill="#bbb"/></svg></div>
  <div class="abs btn">Register Now</div>
</section>

<section>
  <h2 class="abs faq-title">Frequently Asked Questions</h2>
  <div class="abs faq-rule" style="top:825px"></div>
  <div class="abs faq-q" style="top:840px">What is Lorem Ipsum?</div>
  <div class="abs faq-toggle" style="top:841px"><svg width="8" height="8" viewBox="0 0 8 8"><path d="M4 0v8M0 4h8" stroke="#fff" stroke-width="1.4"/></svg></div>

  <div class="abs faq-rule" style="top:872px"></div>
  <div class="abs faq-q is-open" style="top:886px">Why do we use it?</div>
  <div class="abs faq-toggle is-open" style="top:892px"><svg width="8" height="8" viewBox="0 0 8 8"><path d="M0 4h8" stroke="#fff" stroke-width="1.6"/></svg></div>
  <p class="abs faq-a">It is a long established fact that a reader will be distracted by the readable content of a page when looking at its layout. The point of using Lorem Ipsum is that it has a more-or-less normal distribution of letters, as opposed to using 'Content here, content here', making it look like readable English.</p>

  <div class="abs faq-rule" style="top:970px"></div>
  <div class="abs faq-q" style="top:985px">How is this different from TalkMind or other AI tools?</div>
  <div class="abs faq-toggle" style="top:987px"><svg width="8" height="8" viewBox="0 0 8 8"><path d="M4 0v8M0 4h8" stroke="#fff" stroke-width="1.4"/></svg></div>

  <div class="abs faq-rule" style="top:1018px"></div>
  <div class="abs faq-q" style="top:1030px">What's the difference between joining the waitlist and becoming a Builder?</div>
  <div class="abs faq-toggle" style="top:1033px"><svg width="8" height="8" viewBox="0 0 8 8"><path d="M4 0v8M0 4h8" stroke="#fff" stroke-width="1.4"/></svg></div>
  <div class="abs faq-rule" style="top:1065px"></div>
</section>

<footer>
  <div class="abs footer"></div>
  <p class="abs copyright">Copyright © 2025 Corestride Personal Training Studio, All rights reserved</p>
  <span class="abs social" style="left:967px"></span>
  <span class="abs social" style="left:995px"></span>
  <span class="abs social-round"><span style="width:9px;height:9px;background:#fff;border-radius:2px;display:block"></span></span>
</footer>

</body>
</html>
```